Stainless Steel Water Bottle Packaging

We need a design for our cylindrical water bottle packaging.

Please see attached template (500ml cola bottle template .ai file) for exact dimensions.

VORO is defined as the elemental forces of nature embodied in an object or person. The design should be eye catching and draw potential clients in. Although its a cylindrical bottle/box, the front which would face the customer when sitting on a shelf should clearly display our logo.

Industry/Entity Type

Steel

Requirements
Must have
• Designed to the specifications of the attached template (see attached)
• Our VORO Logo (see attached) and website www.vorobottle.example(in smaller font) must appear.
• Size of bottle must appear - '17 oz/500 ml'
• These should appear somewhere:
• 'INULATED DOUBLE-WALL STAINLESS STEEL WATER BOTTLE'
• 'VORO Bottles magically keeps drinks cold for up to 24hrs, hot for 12',
• 'BPA Free'
• 'For every VORO bottle purchased, a portion of proceeds will go towards charity. Each of our colour's have been assigned a specific charity. Please visit www.vorobottle.example to find out which charity you helped support!'
• The Top circle - just our Symbol (flame/drop)
• The bottom circle - 'Inc. Designed in Canada made in China' on the outer edge leaving the middle empty for the UPC code.
• Reference website for the bottle case I'm looking for:
• http://shopkorinday.example/t-flow-lagoon-pink-insulated-water-bottle
Nice to have
• illustration of our water bottle shape (see attached) appearing somewhere on the box is something i had in mind but definitely not necessary.

```html
<!DOCTYPE html>
<html lang="en">
<head>
<meta charset="UTF-8">
<title>VORO Bottle Packaging</title>
<link href="https://fonts.googleapis.com/css2?family=Bebas+Neue&family=Open+Sans:wght@400&display=swap" rel="stylesheet">
<style>
  :root {
    --sky: #2fa6dc;
    --ocean: #0e6fae;
    --deep: #06508c;
    --navy: #0b4a86;
    --gold: #f6c223;
    --gold-light: #fde58a;
    --silver-light: #ececef;
    --silver-dark: #8e8d94;
    --white: #ffffff;
    --cut-line: #d9252a;
  }
  html, body {
    margin: 0;
    padding: 0;
    overflow: hidden;
    background: var(--white);
  }
  .package {
    position: relative;
    width: 774px;
    height: 1200px;
    overflow: hidden;
    background: var(--white);
    font-family: "Bebas Neue", Impact, sans-serif;
    color: var(--white);
  }
  .lids {
    position: absolute;
    top: 0;
    left: 0;
    width: 774px;
    height: 325px;
  }
  .lid-name {
    font-family: "Bebas Neue", Impact, sans-serif;
    font-size: 64px;
    fill: var(--white);
    letter-spacing: 2px;
  }
  .lid-edge-text {
    font-family: "Open Sans", Arial, sans-serif;
    font-size: 10.5px;
    fill: var(--white);
  }
  .wrap {
    position: absolute;
    top: 325px;
    left: 0;
    width: 774px;
    height: 875px;
    background: linear-gradient(180deg, var(--sky) 0%, var(--ocean) 70%);
  }
  .tagline {
    position: absolute;
    left: 14px;
    top: 236px;
    width: 246px;
    margin: 0;
    text-align: center;
    font-size: 26.5px;
    line-height: 1.02;
    font-weight: 400;
  }
  .charity-box {
    position: absolute;
    left: 22px;
    top: 354px;
    width: 232px;
    height: 199px;
    box-sizing: border-box;
    border: 1.5px solid var(--gold);
    border-radius: 15px;
    padding: 8px 6px 0;
    text-align: center;
    font-size: 17px;
    line-height: 1.14;
  }
  .charity-box p { margin: 0; }
  .charity-url {
    display: block;
    color: var(--gold);
    font-size: 25px;
    line-height: 1.05;
    margin: 3px 0 1px;
  }
  .brand-name {
    position: absolute;
    left: 360px;
    top: 490px;
    width: 340px;
    margin: 0;
    text-align: center;
    font-size: 92px;
    line-height: 1;
    letter-spacing: 14px;
    font-weight: 400;
  }
  .band {
    position: absolute;
    left: 0;
    top: 589px;
    width: 774px;
    height: 74px;
    box-sizing: border-box;
    border-top: 6px solid var(--gold);
    border-bottom: 6px solid var(--gold);
    background: linear-gradient(90deg, var(--silver-light) 0%, var(--silver-dark) 30%, var(--silver-light) 55%, var(--silver-dark) 88%, var(--silver-light) 100%);
  }
  .band::before, .band::after {
    content: "";
    position: absolute;
    left: 0;
    width: 100%;
    height: 2px;
    background: var(--gold-light);
  }
  .band::before { top: 0; }
  .band::after { bottom: 0; }
  .band-url {
    position: absolute;
    left: 340px;
    width: 392px;
    top: 9px;
    margin: 0;
    text-align: center;
    color: var(--navy);
    font-size: 44px;
    line-height: 1;
    white-space: nowrap;
  }
  .lower {
    position: absolute;
    left: 0;
    top: 663px;
    width: 774px;
    height: 212px;
    background: linear-gradient(180deg, var(--ocean) 0%, var(--deep) 100%);
  }
  .bpa {
    position: absolute;
    left: 53px;
    top: 92px;
    display: flex;
    align-items: center;
    gap: 4px;
    color: var(--gold);
    font-size: 40px;
    line-height: 1;
  }
  .bpa svg { width: 42px; height: 40px; }
  .product-type {
    position: absolute;
    left: 332px;
    top: 50px;
    width: 400px;
    margin: 0;
    text-align: center;
    font-size: 24px;
    line-height: 0.98;
  }
  .capacity {
    position: absolute;
    left: 332px;
    top: 146px;
    width: 400px;
    margin: 0;
    text-align: center;
    font-size: 40px;
    line-height: 1;
  }
</style>
</head>
<body>
<main class="package">
  <svg class="lids" viewBox="0 0 774 325" aria-label="Lid and base circles">
    <defs>
      <linearGradient id="lidFill" x1="0" y1="0" x2="0" y2="1">
        <stop offset="0" stop-color="#33a8dd"/>
        <stop offset="1" stop-color="#0c5f9c"/>
      </linearGradient>
      <linearGradient id="baseFill" x1="0" y1="0" x2="0" y2="1">
        <stop offset="0" stop-color="#1d8ccb"/>
        <stop offset="1" stop-color="#07508c"/>
      </linearGradient>
      <path id="baseArc" d="M 416.7 190 A 98 98 0 0 0 597.3 190"/>
    </defs>
    <g class="lid-top">
      <circle cx="248" cy="152" r="120" fill="url(#lidFill)" stroke="var(--cut-line)" stroke-width="1"/>
      <text class="lid-name" x="248" y="175" text-anchor="middle">VORO</text>
    </g>
    <g class="lid-base">
      <circle cx="507" cy="152" r="120" fill="url(#baseFill)" stroke="var(--cut-line)" stroke-width="1"/>
      <circle cx="425" cy="152" r="7" fill="none" stroke="var(--cut-line)" stroke-width="1"/>
      <circle cx="588" cy="152" r="7" fill="none" stroke="var(--cut-line)" stroke-width="1"/>
      <text class="lid-edge-text"><textPath href="#baseArc" startOffset="50%" text-anchor="middle">Inc. Designed in Canada made in China</textPath></text>
    </g>
  </svg>

  <section class="wrap">
    <h2 class="tagline">VORO Bottles magically keeps drinks cold for up to 24hrs, hot for 12</h2>

    <div class="charity-box">
      <p>For every VORO bottle purchased, a portion of proceeds will go towards charity. Each of our colour's have been assigned a specific charity. Please visit</p>
      <span class="charity-url">www.vorobottle.example</span>
      <p>to find out which charity you helped support!</p>
    </div>

    <h1 class="brand-name">VORO</h1>

    <div class="band">
      <p class="band-url">www.vorobottle.example</p>
    </div>

    <div class="lower">
      <div class="bpa">
        <svg viewBox="0 0 38 36" aria-hidden="true">
          <path d="M4 33 C10 22 18 14 30 6" fill="none" stroke="#fff" stroke-width="2" stroke-linecap="round"/>
          <path d="M8 28 C4 16 14 4 34 3 C34 20 24 30 8 28 Z" fill="none" stroke="#fff" stroke-width="2" stroke-linejoin="round"/>
        </svg>
        <span>BPA FREE</span>
      </div>
      <p class="product-type">Inulated Double-Wall<br>Stainless Steel Water Bottle</p>
      <p class="capacity">17 OZ/500 ML</p>
    </div>
  </section>
</main>
</body>
</html>
```